Business Folder

I need a fresh, modern design for a business folder. I have our company's colors, logo, and a separate file for just the graphic part of our logo as a design element. No photo, just colors, gradients, and shadows to create depth. I like the idea of a rich grey as the background, however, I realize we'd have to lighten to 'Tax Advisory Services' part of our logo.

The design would just be the 'front' or outside of the folder from Mellowfax. Design file attached. You can find that here under 9 x 12 standard folder, Left and Right Pockets With Slit Both Sides:

https://www.mellowfax-example.com/content.html?id=folderDownloadTemplates&rightMenuId=rightMenu&footerId=bodyFooterStyle6

```html
<!DOCTYPE html>
<html lang="en">
<head>
<meta charset="utf-8">
<title>Norvale Business Folder</title>
<link rel="stylesheet" href="https://fonts.googleapis.com/css2?family=Oswald:wght@500;600&family=Montserrat:wght@400;500;700;800&display=swap">
<style>
  :root {
    --bg: #e4e4e4;
    --paper: #f6f6f6;
    --ink-dark: #3b3b3b;
    --ink-mid: #585858;
    --ink-soft: #7c7c7c;
    --ink-pale: #9a9a9a;
    --text-body: #555555;
    --white: #ffffff;
  }
  * { margin: 0; padding: 0; box-sizing: border-box; }
  html, body { width: 1070px; height: 1200px; overflow: hidden; background: var(--bg); }
  .canvas { position: relative; width: 1070px; height: 1200px; font-family: "Montserrat", sans-serif; }
  .caption {
    position: absolute; font-family: "Montserrat", sans-serif; font-size: 17px;
    color: #222; letter-spacing: 0.5px;
  }
  .caption--outer { left: 135px; top: 22px; }
  .caption--inner { right: 135px; top: 1170px; }
  .spread {
    position: absolute; left: 135px; width: 800px; height: 533px;
    display: flex; box-shadow: 0 10px 28px rgba(0,0,0,0.18);
  }
  .spread--outer { top: 56px; }
  .spread--inner { top: 628px; }
  .panel { width: 400px; height: 533px; display: block; background: var(--paper); }
  .panel + .panel { border-left: 1px solid #dcdcdc; }
  .heading { font-family: "Oswald", sans-serif; font-weight: 600; }
  .body-text { font-family: "Montserrat", sans-serif; }
</style>
</head>
<body>
<div class="canvas">
  <div class="caption caption--outer">OUTER FOLDER</div>

  <div class="spread spread--outer">
    <!-- back cover -->
    <svg class="panel panel--back" viewBox="0 0 400 533" xmlns="http://www.w3.org/2000/svg">
      <rect width="400" height="533" fill="var(--paper)"/>
      <path d="M0,0 H330 V190 Q330,222 300,226 L0,262 Z" fill="var(--ink-dark)"/>
      <path d="M140,150 L270,70 Q290,60 300,78 L300,200 Q298,214 284,216 L180,226 Z" fill="var(--ink-mid)"/>
      <path d="M210,160 L300,110 L300,210 L230,218 Z" fill="var(--ink-soft)" opacity="0.7"/>
      <path d="M135,115 L175,135 L135,155 Z" fill="var(--ink-pale)"/>
      <path d="M0,200 H110 Q130,200 130,214 Q130,228 110,230 L0,244 Z" fill="var(--ink-soft)" opacity="0.6"/>
      <text x="30" y="48" class="heading" font-size="22" fill="var(--white)" letter-spacing="0.5">LOREM IPSUM SIMPLY TEXT</text>

      <text x="70" y="388" class="body-text" font-size="13" fill="var(--text-body)" font-weight="500">GET IN TOUCH</text>
      <line x1="70" y1="395" x2="104" y2="395" stroke="var(--text-body)" stroke-width="1.5"/>
      <circle cx="74" cy="412" r="3.5" fill="var(--text-body)"/>
      <text class="body-text" font-size="9.5" fill="var(--text-body)">
        <tspan x="84" y="415">Block 58A Plot 10B lorem</tspan>
        <tspan x="84" y="427">ipsum simply dummy text ,</tspan>
        <tspan x="84" y="439">Uk - 1234</tspan>
      </text>
      <circle cx="226" cy="366" r="3.5" fill="var(--text-body)"/>
      <text x="236" y="369" class="body-text" font-size="9.5" fill="var(--text-body)">080765432100</text>
      <circle cx="226" cy="382" r="3.5" fill="var(--text-body)"/>
      <text x="236" y="385" class="body-text" font-size="9.5" fill="var(--text-body)">hello@norvale-example.com</text>
      <circle cx="226" cy="398" r="3.5" fill="var(--text-body)"/>
      <text x="236" y="401" class="body-text" font-size="9.5" fill="var(--text-body)">www.norvale-example.com</text>

      <path d="M0,440 L300,495 L260,533 H0 Z" fill="var(--ink-dark)"/>
      <path d="M0,470 L160,533 H0 Z" fill="var(--ink-mid)"/>
      <path d="M0,492 L46,512 L0,533 Z" fill="var(--ink-soft)"/>
    </svg>

    <!-- front cover -->
    <svg class="panel panel--front" viewBox="0 0 400 533" xmlns="http://www.w3.org/2000/svg">
      <rect width="400" height="533" fill="var(--paper)"/>
      <path d="M0,332 Q0,304 30,306 L400,350 V533 H0 Z" fill="var(--ink-dark)"/>
      <path d="M0,470 Q40,440 90,470 L150,533 H0 Z" fill="var(--ink-mid)" opacity="0.8"/>
      <path d="M260,533 L400,470 V533 Z" fill="var(--ink-mid)"/>
      <polygon points="200,14 326,84 326,224 200,294 74,224 74,84" fill="none" stroke="var(--ink-dark)" stroke-width="8"/>
      <polygon points="200,30 312,92 312,216 200,278 88,216 88,92" fill="var(--ink-dark)" stroke="var(--white)" stroke-width="4"/>
      <text x="200" y="168" text-anchor="middle" class="body-text" font-weight="800" font-size="33" fill="var(--white)" letter-spacing="1">NORVALE</text>
      <text x="200" y="190" text-anchor="middle" class="body-text" font-size="10" fill="#d8d8d8" letter-spacing="1.3">TAX ADVISORY SERVICES</text>
      <path d="M300,326 L372,296 Q384,292 382,304 L362,370 Z" fill="var(--ink-mid)"/>
      <path d="M318,330 L368,306 L352,360 Z" fill="var(--ink-soft)"/>
      <text x="40" y="408" class="heading" font-size="54" fill="var(--white)">LOREM</text>
      <text x="42" y="432" class="body-text" font-size="15" fill="var(--white)" letter-spacing="0.5">IPSUM SIMPLY TEXT</text>
      <circle cx="92" cy="492" r="2.5" fill="none" stroke="#cfcfcf"/>
      <line x1="95" y1="492" x2="160" y2="492" stroke="#cfcfcf" stroke-width="0.8"/>
      <text x="240" y="495" text-anchor="middle" class="body-text" font-size="9.5" fill="#dedede" letter-spacing="1">www.norvale-example.com</text>
      <line x1="320" y1="492" x2="372" y2="492" stroke="#cfcfcf" stroke-width="0.8"/>
      <circle cx="375" cy="492" r="2.5" fill="none" stroke="#cfcfcf"/>
    </svg>
  </div>

  <div class="spread spread--inner">
    <!-- inside left with pocket -->
    <svg class="panel panel--inside-left" viewBox="0 0 400 533" xmlns="http://www.w3.org/2000/svg">
      <rect width="400" height="533" fill="var(--paper)"/>
      <rect y="352" width="400" height="181" fill="var(--white)"/>
      <line x1="0" y1="352" x2="400" y2="352" stroke="#d6d6d6"/>
      <path d="M0,400 L160,368 Q184,364 180,384 L168,430 Q164,444 150,442 L0,420 Z" fill="var(--ink-dark)"/>
      <path d="M0,412 L130,432 Q152,436 142,456 L116,516 Q110,533 96,533 H0 Z" fill="var(--ink-pale)"/>
      <path d="M0,440 L86,454 L60,533 H0 Z" fill="var(--ink-soft)" opacity="0.7"/>
      <text x="292" y="462" text-anchor="middle" class="body-text" font-weight="800" font-size="30" fill="var(--ink-dark)">NORVALE</text>
      <text x="292" y="480" text-anchor="middle" class="body-text" font-size="9" fill="var(--ink-dark)" letter-spacing="1.1">TAX ADVISORY SERVICES</text>
    </svg>

    <!-- inside right with pocket -->
    <svg class="panel panel--inside-right" viewBox="0 0 400 533" xmlns="http://www.w3.org/2000/svg">
      <rect width="400" height="533" fill="var(--paper)"/>
      <rect y="352" width="400" height="181" fill="var(--ink-dark)"/>
      <path d="M0,352 H60 L150,533 H0 Z" fill="var(--ink-soft)"/>
      <path d="M60,352 H110 L240,533 H150 Z" fill="var(--ink-mid)"/>
      <rect x="212" y="396" width="150" height="82" rx="7" fill="var(--white)"/>
      <text x="287" y="441" text-anchor="middle" class="body-text" font-size="8" fill="#333" letter-spacing="1">BUSINESS CARD</text>
      <line x1="340" y1="392" x2="368" y2="408" stroke="#9a9a9a" stroke-width="0.8"/>
      <line x1="206" y1="466" x2="232" y2="484" stroke="#9a9a9a" stroke-width="0.8"/>
    </svg>
  </div>

  <div class="caption caption--inner">INNER FOLDER</div>
</div>
</body>
</html>
```